Website for new dental office

I am Dr. Colin Marsh and am building a new dental practice. I specialize in general dentistry. I am young and have a higher end dental practice incorporating very new technologies and would like my website to reflect that. As many dental patients are older, the website must be very easy to navigate. I would like patients to be able to request appointments, and will eventually add on patient information forms (the health history, etc, that you normally fill out in the practice) from my practice management software, so leave an area for that.

Industry/Entity Type

Building

```html
<!DOCTYPE html>
<html lang="en">
<head>
<meta charset="utf-8">
<title>Marsh Dental Cosmetic Dentistry</title>
<link rel="stylesheet" href="https://fonts.googleapis.com/css2?family=Fjalla+One&family=Raleway:wght@400;500;600;700&display=swap">
<style>
:root{
  --purple:#5e2c72;
  --purple-dark:#3c1450;
  --green:#7cc516;
  --green-dark:#5f9d0c;
  --navy:#1f2f4a;
  --blue:#2b6fb8;
  --panel-blue:#5d9bd3;
  --brown:#8a4413;
  --text:#3a3a3a;
  --line:#d9d9d9;
  --footer:#2c3549;
  --footer-text:#a9b2c3;
  --bar:#6a7e9f;
  --peach:#eac9a0;
}
*{margin:0;padding:0;box-sizing:border-box}
html,body{width:1129px;height:1200px;overflow:hidden}
body{position:relative;background:#fff;font-family:'Raleway',sans-serif;color:var(--text)}
.abs{position:absolute}
.hero-bg{left:0;top:0;width:1129px;height:543px;background:linear-gradient(90deg,var(--peach) 0%,#efd6b6 30%,#f6e9dc 60%,#fbf6f0 100%)}
.hero-photo{left:340px;top:129px;width:789px;height:414px;background:radial-gradient(ellipse at 45% 45%,#e2b598 0%,#ecd0bd 35%,rgba(248,240,234,.9) 65%,rgba(255,255,255,0) 100%)}
.topnav{left:150px;top:0;width:827px;height:43px;background:var(--purple)}
.topnav a{position:absolute;top:0;height:43px;display:flex;align-items:center;color:#fff;font-family:'Raleway',sans-serif;font-weight:700;font-size:12.5px;text-decoration:none;text-transform:uppercase}
.topnav .active{background:var(--purple-dark);padding:0 17px;left:0}
.social-dot{position:absolute;top:16px;width:11px;height:11px;border-radius:50%;background:#fff}
.masthead{left:150px;top:43px;width:827px;height:86px;background:#fff}
.brand-mark{left:221px;top:57px;width:26px;height:26px;border-radius:50%;background:#3b8fd9}
.brand-name{left:163px;top:89px;font-family:'Fjalla One',sans-serif;font-size:23px;color:var(--navy)}
.contact-label{font-family:'Raleway',sans-serif;font-size:13.5px;color:#777}
.contact-value{font-family:'Fjalla One',sans-serif;font-size:18.5px;color:#222}
.btn-top{left:766px;top:71px;width:191px;height:35px;background:var(--green);border-bottom:3px solid var(--green-dark);color:#fff;font-family:'Fjalla One',sans-serif;font-size:13.5px;display:flex;align-items:center;justify-content:center;gap:8px}
.hero-title{left:152px;top:240px;color:var(--brown);font-family:'Raleway',sans-serif;line-height:1}
.hero-title .s{font-size:28px;display:block}
.hero-title .l{font-size:43px;display:block;margin:2px 0}
.hero-copy{left:152px;top:350px;width:270px;font-size:11.5px;line-height:18.5px;color:#222}
.btn-hero{left:152px;top:454px;width:331px;height:54px;border-radius:27px;background:#fff;box-shadow:0 2px 5px rgba(0,0,0,.15)}
.btn-hero .pill{position:absolute;left:4px;top:4px;width:278px;height:46px;border-radius:23px;background:var(--purple);color:#fff;font-family:'Fjalla One',sans-serif;font-size:25px;line-height:46px;padding-left:17px}
.welcome-small{left:151px;top:582px;font-family:'Fjalla One',sans-serif;font-size:18px;color:var(--navy)}
.welcome-big{left:151px;top:606px;font-family:'Fjalla One',sans-serif;font-size:24px;font-weight:400;color:var(--blue)}
.doctor-photo{left:150px;top:663px;width:193px;height:297px;border-radius:90px 90px 10px 10px;background:linear-gradient(180deg,#e8c3a5 0%,#f1ece8 30%,#ffffff 60%,#f3f3f5 100%)}
.meet{left:276px;top:720px;font-size:12px;color:#333;line-height:16px}
.meet .name{font-size:13.5px;color:#444}
.meet .dds{display:block;text-align:right;font-size:10.5px;color:#666}
.about{left:389px;top:701px;width:285px;font-size:11.5px;line-height:17.7px;color:#555}
.services{left:389px;top:856px;list-style:none}
.services li{font-size:11.5px;font-weight:600;color:#333;height:25px;display:flex;align-items:center;gap:12px}
.booking{left:714px;top:612px;width:263px;height:341px;background:#f1f1f1}
.booking-head{height:33px;background:var(--panel-blue);color:#fff;font-size:12.5px;font-weight:600;display:flex;align-items:center;gap:9px;padding-left:13px}
.field{position:absolute;left:14px;width:234px;height:35px;background:#fff;border:1px solid var(--line);font-size:11px;color:#888;display:flex;align-items:center;padding-left:12px}
.field svg{position:absolute;right:10px}
.field .select-btn{position:absolute;right:0;top:0;width:35px;height:33px;border-left:1px solid var(--line);display:flex;align-items:center;justify-content:center}
.field .select-btn svg{position:static}
.submit{position:absolute;left:16px;top:293px;width:232px;height:32px;background:var(--green);border-bottom:3px solid var(--green-dark);color:#fff;font-weight:700;font-size:13px;display:flex;align-items:center;justify-content:center}
.site-footer{left:0;top:997px;width:1129px;height:169px;background:var(--footer)}
.footer-col{position:absolute;top:1016px;color:var(--footer-text);font-size:11px;line-height:15px}
.footer-col h4{color:#fff;font-size:12.5px;font-weight:600;margin-bottom:14px;text-transform:uppercase}
.testimonial{font-size:10.5px;line-height:15px}
.footer-row{display:flex;align-items:center;gap:14px}
.contact-rows .footer-row{margin-bottom:20px}
.social-rows .footer-row{height:17px;margin-bottom:13px}
.nav-list{list-style:none;line-height:19px}
.social-sq{width:17px;height:17px;background:#8b96ab;border-radius:2px;flex:none}
.bottom-bar{left:0;top:1166px;width:1129px;height:34px;background:var(--bar);color:#1e2638;font-size:9.5px}
</style>
</head>
<body>
<div class="abs hero-bg"></div>
<div class="abs hero-photo" role="img" aria-label="Photo of a smiling young couple embracing"></div>

<nav class="abs topnav">
  <a class="active" href="#">Home</a>
  <a href="#" style="left:83px">Our Staff</a>
  <a href="#" style="left:179px">Services</a>
  <a href="#" style="left:265px">Our Office</a>
  <a href="#" style="left:363px">Patient Resources</a>
  <a href="#" style="left:509px">Contact Us</a>
  <span class="social-dot" style="left:680px"></span>
  <span class="social-dot" style="left:719px"></span>
  <span class="social-dot" style="left:757px"></span>
  <span class="social-dot" style="left:795px"></span>
</nav>

<header class="abs masthead"></header>
<div class="abs brand-mark"></div>
<div class="abs brand-name">Colin Marsh, (DDS)</div>
<svg class="abs" style="left:381px;top:89px" width="18" height="16" viewBox="0 0 18 16"><path d="M2 5c0-3 14-3 14 0v2h-4V5H6v2H2z" fill="#888"/><rect x="4" y="8" width="10" height="7" rx="1" fill="#aaa"/></svg>
<div class="abs contact-label" style="left:405px;top:67px">(Call us)</div>
<div class="abs contact-value" style="left:405px;top:85px">+1800-555-01234</div>
<svg class="abs" style="left:573px;top:87px" width="18" height="17" viewBox="0 0 18 17"><rect x="1" y="1" width="16" height="15" fill="#bbb"/><path d="M1 1l8 7 8-7" stroke="#fff" fill="none" stroke-width="1.4"/></svg>
<div class="abs contact-label" style="left:599px;top:67px">(E-mail)</div>
<div class="abs contact-value" style="left:599px;top:85px">info@marshdds.com</div>
<div class="abs btn-top">
  <svg width="17" height="15" viewBox="0 0 17 15"><rect x="1" y="2" width="15" height="12" fill="none" stroke="#fff" stroke-width="1.5"/><path d="M1 6h15M5 0v4M12 0v4" stroke="#fff" stroke-width="1.5"/></svg>
  REQUEST AN APPOINMENT
</div>

<div class="abs hero-title"><span class="s">Your</span><span class="l">wellness</span><span class="s">starts today</span></div>
<p class="abs hero-copy">Lorem ipsum dolor sit amet, consectetur adipisicing elit, sed do eiusmod tempor incididunt ut labore et dolore magna aliqua</p>
<div class="abs btn-hero">
  <div class="pill">REQUEST AN APPOINMENT</div>
  <svg style="position:absolute;left:288px;top:12px" width="33" height="32" viewBox="0 0 33 32"><rect x="2" y="5" width="22" height="20" rx="2" fill="none" stroke="#5e2c72" stroke-width="2.5"/><path d="M2 11h22M8 2v6M18 2v6" stroke="#5e2c72" stroke-width="2.5"/><circle cx="24" cy="23" r="8" fill="#5e2c72"/><path d="M20 23l3 3 5-5" stroke="#fff" stroke-width="2" fill="none"/></svg>
</div>

<div class="abs welcome-small">Welcome to</div>
<h1 class="abs welcome-big">Marsh Dental Cosmetic Dentistry</h1>
<div class="abs doctor-photo" role="img" aria-label="Portrait of the dentist in a white coat with a stethoscope"></div>
<div class="abs meet">Meet Our<br><span class="name">Dr. Colin Marsh</span><span class="dds">DDS</span></div>
<p class="abs about">At vero eos et accusamus et iusto odio dignissimos ducimus qui blanditiis praesentium voluptatum deleniti atque corrupti quos dolores et quas molestias excepturi sint occaecati cupiditate non provident, similique sunt in culpa qui officia deserunt mollitia animi, id est laborum et dolorum fuga. Et harum quidem rerum facilis est et expedita distinctio. Nam libero tempore, cum soluta nobis est eligendi optio cumque.</p>
<ul class="abs services">
  <li><svg width="9" height="8" viewBox="0 0 9 8"><path d="M0 4h8M5 1l3 3-3 3" stroke="#888" fill="none"/></svg>Do-Preventive</li>
  <li><svg width="9" height="8" viewBox="0 0 9 8"><path d="M0 4h8M5 1l3 3-3 3" stroke="#888" fill="none"/></svg>Restorative</li>
  <li><svg width="9" height="8" viewBox="0 0 9 8"><path d="M0 4h8M5 1l3 3-3 3" stroke="#888" fill="none"/></svg>Cosmetic</li>
  <li><svg width="9" height="8" viewBox="0 0 9 8"><path d="M0 4h8M5 1l3 3-3 3" stroke="#888" fill="none"/></svg>Tooth Replacement</li>
</ul>

<section class="abs booking">
  <div class="booking-head"><svg width="12" height="13" viewBox="0 0 12 13"><rect x="1" y="3" width="10" height="9" fill="#fff"/><rect x="3" y="0" width="6" height="4" fill="#fff"/></svg>Book an Appointment</div>
  <div class="field" style="top:48px">Select Department<span class="select-btn"><svg width="11" height="11" viewBox="0 0 11 11"><rect x=".5" y=".5" width="10" height="10" fill="none" stroke="#555"/><path d="M3 4h5L5.5 7z" fill="#333"/></svg></span></div>
  <div class="field" style="top:97px">Your Full Name (Required)<svg width="12" height="13" viewBox="0 0 12 13"><circle cx="6" cy="4" r="3.3" fill="#ccc"/><path d="M0 13c0-4 12-4 12 0z" fill="#ccc"/></svg></div>
  <div class="field" style="top:146px">Your Email<svg width="14" height="11" viewBox="0 0 14 11"><rect width="14" height="11" fill="#ccc"/><path d="M0 0l7 6 7-6" stroke="#fff" fill="none"/></svg></div>
  <div class="field" style="top:195px">Your Phone (Required)<svg width="11" height="12" viewBox="0 0 11 12"><path d="M2 0l3 3-1.5 2a7 7 0 003 3L8 7l3 3-2 2C4 12 0 7 0 2z" fill="#ccc"/></svg></div>
  <div class="field" style="top:243px">Date Of Appoinment<svg width="14" height="13" viewBox="0 0 14 13"><rect x=".5" y="2" width="13" height="10.5" fill="none" stroke="#bbb"/><path d="M.5 5h13M4 0v3M10 0v3" stroke="#bbb"/></svg></div>
  <div class="submit">SUBMIT</div>
</section>

<footer class="abs site-footer"></footer>
<div class="footer-col" style="left:150px;width:185px">
  <h4>What People Say's</h4>
  <p class="testimonial">"Lorem ipsum dolor sit amet, consectetur adipisicing elit, sed do eiusmod tempor incididunt ut labore et dolore magna aliqua"</p>
  <p style="color:#fff;margin-top:10px">- John Doe<br>Finibus Bonorum et Malorum</p>
</div>
<div class="footer-col contact-rows" style="left:361px">
  <h4>Contact Info</h4>
  <div class="footer-row"><svg width="16" height="11" viewBox="0 0 16 11"><rect width="16" height="11" fill="#8b96ab"/><path d="M0 0l8 6 8-6" stroke="#2c3549" fill="none"/></svg>info@marshdds.com</div>
  <div class="footer-row"><svg width="14" height="14" viewBox="0 0 11 12"><path d="M2 0l3 3-1.5 2a7 7 0 003 3L8 7l3 3-2 2C4 12 0 7 0 2z" fill="#8b96ab"/></svg>+1800-555-0199</div>
  <div class="footer-row" style="align-items:flex-start"><svg width="14" height="18" viewBox="0 0 14 18"><path d="M7 0a7 7 0 017 7c0 5-7 11-7 11S0 12 0 7a7 7 0 017-7z" fill="#8b96ab"/><circle cx="7" cy="7" r="2.5" fill="#2c3549"/></svg><span>95 Lorem ipsum, Suite<br>Stree Lorem, 45 BC</span></div>
</div>
<div class="footer-col" style="left:574px;width:210px">
  <h4>Navigation</h4>
  <ul class="nav-list" style="float:left;width:98px"><li>Home</li><li>Our Staff</li><li>Services</li><li>Our Office</li><li>Patient Resources</li><li>Contact us</li></ul>
  <ul class="nav-list" style="float:left"><li>Do-Preventive</li><li>Restorative</li><li>Cosmetic</li><li>Tooth Replacement</li></ul>
</div>
<div class="footer-col social-rows" style="left:818px">
  <h4>Stay Connected With Us!</h4>
  <div class="footer-row"><span class="social-sq"></span>Facepage</div>
  <div class="footer-row"><span class="social-sq"></span>Chirper</div>
  <div class="footer-row"><span class="social-sq"></span>Circles +</div>
  <div class="footer-row"><span class="social-sq"></span>Worklink</div>
</div>
<div class="abs bottom-bar">
  <span style="position:absolute;left:150px;top:11px">Colin Marsh,DDS &nbsp;Copyright © 2014 - All Rights Reserved</span>
  <span style="position:absolute;right:152px;top:11px">Privacy Policy | Sitemap</span>
</div>
</body>
</html>
```